Prayer Service 12.28.2013

I need a flyer designed for a Christian prayer service. The title and theme is:
"Total and Complete Surrender for Total and Complete Deliverance!"
1. You have creative freedom with imagery and typography
2. I need a quick turnaround time
FLYER DETAILS:
A prayer, anointing, and deliverance all night prayer service, at Brightwater Assembly.
Saturday December 28 2013 from 9pm-6am.
Special guest speakers, prayer,anointing,and deliverance sessions.
For more information contact Sis Dorothy Whitfield at Brightwater Assembly 555 634 1297 Ext. 4816 or Monica Shaw at 555 802-3941

```html
<!DOCTYPE html>
<html lang="en">
<head>
<meta charset="utf-8">
<title>Total Surrender for Complete Deliverance</title>
<link rel="stylesheet" href="https://fonts.googleapis.com/css2?family=Yanone+Kaffeesatz:wght@600&family=Roboto:wght@300;400&family=Arimo&display=swap">
<style>
  :root {
    --page-bg: #1a1410;
    --sky-deep: #4cc0e0;
    --sky-mid: #8fd4ea;
    --sky-pale: #d9f1f8;
    --glow: #ffffff;
    --title-white: #ffffff;
    --teal-dark: #1d4656;
    --ink: #14212a;
  }
  * { margin: 0; padding: 0; box-sizing: border-box; }
  html, body {
    width: 1157px;
    height: 1200px;
    overflow: hidden;
    background: var(--page-bg);
  }
  .flyer {
    position: absolute;
    left: 130px;
    top: 20px;
    width: 796px;
    height: 1030px;
    transform: scale(1.126);
    transform-origin: top left;
    overflow: hidden;
    background:
      radial-gradient(circle at 88% 5%, var(--glow) 0, rgba(255,255,255,0.85) 8%, rgba(255,255,255,0) 40%),
      linear-gradient(165deg, var(--sky-deep) 0%, var(--sky-mid) 35%, var(--sky-pale) 60%, var(--sky-mid) 85%, var(--sky-deep) 100%);
  }
  .prayer-art {
    position: absolute;
    left: 220px;
    top: 0;
    width: 420px;
    height: 900px;
    background: radial-gradient(ellipse at 50% 45%, rgba(235,246,250,0.75) 0%, rgba(200,230,240,0.45) 45%, rgba(255,255,255,0) 75%);
  }
  .title-line {
    position: absolute;
    left: 64px;
    font-family: "Yanone Kaffeesatz", "Arial Narrow", sans-serif;
    font-weight: 600;
    font-size: 112px;
    line-height: 1;
    color: var(--title-white);
    letter-spacing: 1px;
    text-shadow: 1px 2px 3px rgba(0,40,60,0.35);
  }
  .title-line--first { top: 214px; }
  .title-line--second { top: 326px; }
  .title-accent {
    position: absolute;
    left: 66px;
    top: 419px;
    font-family: "Roboto", Arial, sans-serif;
    font-weight: 300;
    font-size: 138px;
    line-height: 1;
    letter-spacing: -2px;
    color: var(--teal-dark);
  }
  .details {
    position: absolute;
    left: 77px;
    width: 710px;
    font-family: "Arimo", Arial, sans-serif;
    font-size: 23px;
    line-height: 31px;
    color: var(--ink);
  }
  .details--about { top: 591px; }
  .details--when { top: 684px; }
  .details--contact { top: 809px; }
  .contact-numbers {
    position: absolute;
    left: 77px;
    top: 876px;
    font-family: "Arimo", Arial, sans-serif;
    font-size: 36px;
    line-height: 47px;
    color: var(--ink);
  }
</style>
</head>
<body>
  <main class="flyer">
    <div class="prayer-art" role="img" aria-label="Soft photograph of hands folded in prayer with rays of light"></div>

    <h1>
      <span class="title-line title-line--first">Total Surrender</span>
      <span class="title-line title-line--second">for Complete</span>
      <span class="title-accent">Deliverance</span>
    </h1>

    <p class="details details--about">A prayer, anointing, and deliverance all night prayer service,<br>at Brightwater Assembly.</p>
    <p class="details details--when">Saturday December 28 2013 from 9pm-6am.<br>Special guest speakers, prayer,anointing,<br>and deliverance sessions.</p>
    <p class="details details--contact">For more information contact Sis Dorothy Whitfield at<br>Brightwater Assembly</p>
    <p class="contact-numbers">555 634 1297 Ext. 4816 or<br>Monica Shaw at 555 802-3941</p>
  </main>
</body>
</html>
```